Letterhead Design Project

We have recently updated our corporate logo and are seeking a new letterhead template.

Attached is the new logo and the old letterhead.

PLEASE DO NOT USE OUR EXISTING WEB SITE FOR INSPIRATION as we are redesigning it.

Target Market(s)

Executives, search professionals, technical and scientific professionals

Industry/Entity Type

Seeking

```html
<!DOCTYPE html>
<html lang="en">
<head>
<meta charset="utf-8">
<title>HelixSeek Stationery</title>
<link href="https://fonts.googleapis.com/css2?family=Nunito+Sans:wght@400;700&display=swap" rel="stylesheet">
<style>
  :root {
    --brand-blue: #2a93c8;
    --liner-blue: #8cc4e3;
    --paper: #ffffff;
    --ink: #333333;
    --backdrop: #1c1c1c;
  }
  * { margin: 0; padding: 0; box-sizing: border-box; }
  html, body { width: 1200px; height: 1000px; overflow: hidden; }
  body {
    background: var(--backdrop);
    font-family: "Nunito Sans", Arial, sans-serif;
    position: relative;
  }
  .brand-mark {
    display: flex; align-items: center; justify-content: center; gap: 8px;
    color: var(--brand-blue); font-weight: 700; line-height: 1;
  }
  .brand-mark .dot { border-radius: 50%; background: var(--brand-blue); flex: none; }
  .brand-mark.large { font-size: 30px; }
  .brand-mark.large .dot { width: 44px; height: 44px; }

  .contact-block { text-align: center; color: var(--ink); }
  .contact-block .brand-mark { font-size: 15px; gap: 5px; margin-bottom: 8px; }
  .contact-block .brand-mark .dot { width: 16px; height: 16px; }
  .contact-block p { font-size: 8px; line-height: 1.3; }
  .contact-block .web strong { font-weight: 700; }

  .letterhead {
    position: absolute; left: 73px; top: 121px;
    width: 530px; height: 749px;
    background: var(--paper);
  }
  .letterhead .header-mark { position: absolute; top: 48px; left: 0; right: 0; }
  .letterhead .contact-block { position: absolute; left: 0; right: 0; bottom: 22px; }

  .envelope-back {
    position: absolute; left: 611px; top: 122px;
    width: 550px; height: 258px;
    background: var(--brand-blue);
  }
  .envelope-back .brand-mark {
    position: absolute; left: 0; right: 0; top: 102px; color: var(--paper);
  }
  .envelope-back .brand-mark .dot { background: var(--paper); }

  .envelope-front {
    position: absolute; left: 611px; top: 612px;
    width: 548px; height: 258px;
    background: var(--paper);
  }
  .envelope-front .feature-mark { position: absolute; left: 0; right: 0; top: 112px; }

  .open-envelope {
    position: absolute; left: 572px; top: 252px;
    width: 580px; height: 460px;
    filter: drop-shadow(0 6px 10px rgba(0,0,0,0.45));
  }
  .open-envelope svg { position: absolute; inset: 0; }
  .open-envelope .contact-block {
    position: absolute; left: 0; right: 0; top: 346px;
  }
</style>
</head>
<body>
  <section class="letterhead">
    <div class="brand-mark large header-mark"><span class="dot"></span>HelixSeek</div>
    <div class="contact-block">
      <div class="brand-mark"><span class="dot"></span>HelixSeek</div>
      <p>Voice: 555.014.0100 /Fax: 555.014.0100</p>
      <p>420 Harbor Lane - Suite 12, Millbrook, MA 01999</p>
      <p class="web">www.<strong>helixseek</strong>.com</p>
    </div>
  </section>

  <section class="envelope-back">
    <div class="brand-mark large"><span class="dot"></span>HelixSeek</div>
  </section>

  <section class="envelope-front">
    <div class="brand-mark large feature-mark"><span class="dot"></span>HelixSeek</div>
  </section>

  <section class="open-envelope">
    <svg viewBox="0 0 580 460" width="580" height="460" role="img" aria-label="Open envelope whose flap and inner liner carry a repeating brand pattern in blue on white">
      <rect x="0" y="215" width="580" height="245" fill="#ffffff"/>
      <polygon points="0,215 118,2 462,2 580,215" fill="#ffffff"/>
      <polygon points="6,213 121,8 459,8 574,213" fill="var(--liner-blue)"/>
      <polygon points="0,215 290,326 580,215" fill="var(--liner-blue)"/>
    </svg>
    <div class="contact-block">
      <div class="brand-mark"><span class="dot"></span>HelixSeek</div>
      <p>Voice: 555.014.0100 /Fax: 555.014.0100</p>
      <p>420 Harbor Lane - Suite 12, Millbrook, MA 01999</p>
      <p class="web">www.<strong>helixseek</strong>.com</p>
    </div>
  </section>
</body>
</html>
```